Law Firm Needs a Stationery Design

We need a stationery design for a law firm based in the East African region called 'Mbweteka Olinyo & Company Advocates'. We are a law firm specializing in commercial, public and constitutional law. Our practice areas include Telecommunications Law, Mining Law, Oil and Energy Law, Real Estate and Land Development Law, Employment Law, Family Law, Civil and Criminal Litigation, Constitutional Law, Company Secretariat and more. We represent a wide variety of clients, ranging from individuals to corporations and approach each case with full attention, dedication and legal acumen in order to protect the interests of our clients. The final stationary design should communicate innovation and expertise to meet our clients’ legal needs.
Target Market(s)
New clients, current and former clients, other lawyers in and outside of our practice area, or other professionals, contacts and centers of influence within the region
Industry/Entity Type
Real Estate
Colors
Designer to choose colors to be used in the design.
Look and feel
Each slider illustrates characteristics of the customer's brand and the style your logo design should communicate.

```html
<!DOCTYPE html>
<html lang="en">
<head>
<meta charset="utf-8">
<title>Mbweteka Olinyo &amp; Company Advocates — Stationery</title>
<link href="https://fonts.googleapis.com/css2?family=Cinzel:wght@400&family=Crimson+Text:ital,wght@0,400;0,600;1,600&family=Great+Vibes&family=Josefin+Sans:wght@400&display=swap" rel="stylesheet">
<style>
  :root{
    --bg-light:#d7ecf1;
    --bg-edge:#bcdde5;
    --slate:#688a99;
    --slate-dark:#557583;
    --paper:#ffffff;
    --ink:#3a3a3a;
    --swoosh:#ffffff;
  }
  *{margin:0;padding:0;box-sizing:border-box}
  html,body{width:1200px;height:1168px;overflow:hidden}
  body{
    position:relative;
    background:radial-gradient(ellipse at 50% 40%,var(--bg-light) 0%,var(--bg-edge) 100%);
    font-family:"Crimson Text",Georgia,serif;
    color:var(--ink);
  }
  .piece{position:absolute;background:var(--paper);overflow:hidden}
  .piece svg.band{position:absolute;left:0;top:0;width:100%;height:100%}
  .wordmark{font-family:"Cinzel",serif;color:var(--slate);text-align:center;line-height:1.05;font-weight:400}
  .wordmark.light{color:var(--paper)}

  /* Letterhead */
  .letterhead{left:122px;top:75px;width:451px;height:613px}
  .letterhead .wordmark{position:absolute;left:38px;top:42px;width:90px;font-size:8px}
  .letterhead .subline{position:absolute;left:38px;top:80px;width:90px;text-align:center;font-family:"Cinzel",serif;font-size:5px;color:var(--slate);line-height:1.3}
  .mission-title{position:absolute;left:0;width:100%;top:158px;text-align:center;font-family:"Josefin Sans",sans-serif;font-size:15px;letter-spacing:.5px;color:#333}
  .mission-text{position:absolute;left:62px;top:202px;width:328px;font-size:6.4px;line-height:11.2px;text-align:justify;color:#444}
  .signature{position:absolute;left:322px;top:322px;width:72px;height:22px;background:#eef2f4}
  .sign-caption{position:absolute;left:300px;top:345px;width:92px;text-align:right;font-size:5.5px;color:#444}
  .letter-footer{position:absolute;left:0;width:100%;top:586px;text-align:center;font-size:8px;color:var(--paper);letter-spacing:.2px}
  .letter-footer b{font-weight:600}
  .letter-footer span{margin:0 14px}

  /* Brand block */
  .brand{position:absolute;left:640px;top:100px;width:400px;text-align:center}
  .brand .wordmark{font-size:28px;letter-spacing:.5px}
  .brand .tagline{margin-top:80px;font-family:"Cinzel",serif;font-size:13px;color:var(--slate);letter-spacing:.4px}
  .brand .title{margin-top:22px;font-family:"Cinzel",serif;font-size:22px;color:var(--slate);letter-spacing:1.5px}

  /* Business cards */
  .card-front{left:652px;top:347px;width:182px;height:112px}
  .card-front .wordmark{position:absolute;top:14px;left:0;width:100%;font-size:8px}
  .card-front .tag{position:absolute;top:43px;width:100%;text-align:center;font-family:"Cinzel",serif;font-size:4.5px;color:var(--slate)}
  .card-front .details{position:absolute;top:69px;width:100%;text-align:center;color:var(--paper);font-size:5px;line-height:6px}
  .card-front .details .firm{font-family:"Cinzel",serif;font-size:5.5px;margin-bottom:2px}
  .card-front .details .name{font-style:italic;font-weight:600;font-size:7px}
  .card-back{left:652px;top:501px;width:182px;height:112px;background:var(--slate)}
  .card-back .wordmark{position:absolute;top:38px;left:0;width:100%;font-size:9px}
  .card-back .tag{position:absolute;top:75px;width:100%;text-align:center;font-family:"Cinzel",serif;font-size:4.5px;color:var(--paper)}

  /* Compliments slip */
  .comp-slip{left:122px;top:712px;width:444px;height:209px}
  .comp-slip .greeting{position:absolute;left:12px;top:148px;font-family:"Great Vibes",cursive;font-size:36px;color:var(--paper)}
  .comp-slip .wordmark{position:absolute;left:340px;top:160px;width:88px;font-size:7.5px}
  .comp-slip .tag{position:absolute;left:330px;top:188px;width:108px;text-align:center;font-family:"Cinzel",serif;font-size:4px;color:var(--paper)}

  /* Envelope */
  .envelope-flap{position:absolute;left:585px;top:768px;width:443px;height:160px;background:var(--slate-dark)}
  .envelope{left:585px;top:918px;width:443px;height:162px}
  .return-label{position:absolute;left:316px;top:104px;font-size:4.8px;line-height:6.2px;color:#222}
  .return-label .head{font-weight:600;margin-bottom:4px}

  /* DL card */
  .dl-card{left:643px;top:685px;width:444px;height:208px}
  .dl-card .wordmark{position:absolute;left:338px;top:160px;width:90px;font-size:7.5px}
  .dl-card .tag{position:absolute;left:330px;top:188px;width:108px;text-align:center;font-family:"Cinzel",serif;font-size:4px;color:var(--paper)}
</style>
</head>
<body>

<!-- Letterhead -->
<section class="piece letterhead">
  <svg class="band" viewBox="0 0 451 613" preserveAspectRatio="none" aria-hidden="true">
    <path d="M0,534 C150,548 340,552 451,538 L451,613 L0,613 Z" fill="var(--slate)"/>
    <path d="M0,534 C160,542 340,536 451,520 L451,538 C340,552 150,548 0,534 Z" fill="var(--slate)"/>
    <path d="M200,566 C280,568 360,560 451,528 C380,556 300,570 200,566 Z" fill="var(--swoosh)"/>
  </svg>
  <div class="wordmark">Mbweteka Olinyo<br>&amp; Company Advocates</div>
  <div class="subline">The Law Offices of<br>Commercial, Public &amp; Constitutional Law</div>
  <h1 class="mission-title">OUR MISSION</h1>
  <p class="mission-text">Lorem ipsum dolor sit amet, consectetur adipiscing elit. Donec orci purus, luctus vitae dignissim eu, iaculis sed purus. Vivamus faucibus, ipsum nec aliquet viverra, leo mauris condimentum ligula, sit amet sagittis enim ligula quis arcu. Nam egestas tortor id nisi porttitor mattis. In tortor ante, ultricies in suscipit a, tempus non massa. Vivamus et auctor mi. Fusce vel massa nulla. Phasellus nec eros mauris, et scelerisque orci. Donec malesuada orci vitae nulla accumsan porta a id massa. Quisque accumsan iaculis magna sit amet fringilla. Maecenas consequat, magna eget tincidunt semper, odio nibh rutrum mi, id feugiat ante nisi eu risus. Vestibulum nunc orci, rhoncus a placerat in, ultricies in mi. Cras mattis varius eros, vel fringilla nisi suscipit eget.</p>
  <div class="signature" role="img" aria-label="Handwritten signature of Amani Wekesa"></div>
  <div class="sign-caption">Amani Wekesa, Co-Founder &amp; CEO</div>
  <div class="letter-footer"><b>t:</b> 0700 555 210<span>||</span><b>e:</b> info@mbwetekaolinyo.com<span>||</span><b>w:</b> www.mbwetekaolinyo.com</div>
</section>

<!-- Brand identity title -->
<div class="brand">
  <div class="wordmark">Mbweteka Olinyo<br>&amp; Company Advocates</div>
  <div class="tagline">Commercial, Public and Constitutional law</div>
  <div class="title">Branding Identity</div>
</div>

<!-- Business card front -->
<section class="piece card-front">
  <svg class="band" viewBox="0 0 182 112" preserveAspectRatio="none" aria-hidden="true">
    <path d="M0,50 C60,60 140,58 182,44 L182,112 L0,112 Z" fill="var(--slate)"/>
  </svg>
  <div class="wordmark">Mbweteka Olinyo<br>&amp; Company Advocates</div>
  <div class="tag">Commercial, Public and Constitutional law</div>
  <div class="details">
    <div class="firm">Mbweteka Olinyo &amp; Company Advocates</div>
    <div class="name">Amani Wekesa</div>
    <div>amani.wekesa@mbwetekaolinyo.com</div>
    <div>Cell: 0700 555 211</div>
  </div>
</section>

<!-- Business card back -->
<section class="piece card-back">
  <div class="wordmark light">Mbweteka Olinyo<br>&amp; Company Advocates</div>
  <div class="tag">Commercial, Public and Constitutional law</div>
</section>

<!-- Compliments slip -->
<section class="piece comp-slip">
  <svg class="band" viewBox="0 0 444 209" preserveAspectRatio="none" aria-hidden="true">
    <path d="M0,112 C160,118 350,132 444,112 L444,209 L0,209 Z" fill="var(--slate)"/>
    <path d="M190,146 C270,150 350,142 444,116 C370,146 280,154 190,146 Z" fill="var(--swoosh)"/>
  </svg>
  <div class="greeting">With Compliments</div>
  <div class="wordmark light">Mbweteka Olinyo<br>&amp; Company Advocates</div>
  <div class="tag">Commercial, Public and Constitutional law</div>
</section>

<!-- Envelope -->
<div class="envelope-flap" aria-hidden="true"></div>
<section class="piece envelope">
  <div class="return-label">
    <div class="head">IF UNDELIVERED, RETURN TO:</div>
    <div>Mbweteka Olinyo &amp; Company Advocates</div>
    <div style="margin-top:4px">P. O. Box 123-00000,</div>
    <div>Your Street Here,</div>
    <div>City, Country.</div>
  </div>
</section>

<!-- DL card -->
<section class="piece dl-card">
  <svg class="band" viewBox="0 0 444 208" preserveAspectRatio="none" aria-hidden="true">
    <path d="M0,108 C150,122 350,132 444,116 L444,208 L0,208 Z" fill="var(--slate)"/>
    <path d="M188,146 C270,150 350,144 444,118 C370,148 280,154 188,146 Z" fill="var(--swoosh)"/>
  </svg>
  <div class="wordmark light">Mbweteka Olinyo<br>&amp; Company Advocates</div>
  <div class="tag">Commercial, Public and Constitutional law</div>
</section>

</body>
</html>
```